TaviLo Gastronomic Social Network

Tavi Lo is a Gastronomic Social Network that is focused on the relationship between restaurants and customers, creating new channels to communicate with themselves and developing new tools to modernize the classic menus. In Tavi Lo people will see images, videos and texts related on gastronomy shared by the bests restaurants of their cities in real time. Therefore the users will feel how easy is to choose a new restaurant only few minutes before leaving their homes and how useful is to choose a meal with the images of the digital menu in order to have the best experience possible.

Target Market(s)

The direct customers of the company are the restaurants, who pay monthly to post marketing content and their digital menu. The profile of the clients will not be too restrictive: from a restaurant that offers live music and drinks to a classic and expensive restaurant.

The final users of the product are families, couples, professionals and everyone who is interested in discovering new restaurants and good gastronomy.

Requirements
Must have
• We have the idea that after the splash screen show the last registered plates from the restaurants like in snapreel story. On the story we will show the plate for the current time like lunch or dinner, a logo of the restaurant, a small description and the price.
• When selected the plate the user will be redirected to a page will restaurant details showing the selected plate as first item on restaurant menu.
• For each plate we will have a page description showing ingredients, price, harmonization and button to reserve a table.
• Reserve a table is a page for reservation.
• Also we have a page for customer info, last selected plates and restaurants.

```html
<!DOCTYPE html>
<html lang="en">
<head>
<meta charset="utf-8">
<title>Tavi Lo – App Screens</title>
<link href="https://fonts.googleapis.com/css2?family=Poppins:wght@400;500;600;700&display=swap" rel="stylesheet">
<style>
:root{
  --plum:#5b2142;
  --plum-dark:#46102f;
  --orange:#f6a21e;
  --green:#6f9a2c;
  --ink:#1f1f1f;
  --muted:#666;
  --light:#f2f2f2;
  --line:#dcdcdc;
  --white:#fff;
}
*{box-sizing:border-box;margin:0;padding:0}
html,body{width:1200px;height:1200px;overflow:hidden;background:var(--white);font-family:'Poppins',sans-serif;color:var(--ink)}
.stage{position:absolute;left:0;top:0;width:1500px;height:1500px;transform:scale(.8);transform-origin:0 0}
.abs{position:absolute}
.brand{position:absolute;left:150px;top:130px;width:280px;text-align:center;font-size:46px;font-weight:500;color:var(--plum)}
.label-big{position:absolute;font-size:42px;font-weight:400;color:#222}
.dash-h{position:absolute;border-top:1.5px dashed #555}
.dash-v{position:absolute;border-left:1.5px dashed #555}
.note{position:absolute;font-size:17px;color:#222}
.screen{position:absolute;width:440px;background:var(--white);border-radius:42px;overflow:hidden;box-shadow:0 6px 24px rgba(0,0,0,.18)}
.header{position:absolute;left:0;top:0;width:100%;background:var(--plum)}
.time{position:absolute;left:38px;top:20px;color:#fff;font-size:18px;font-weight:500}
.status{position:absolute;right:20px;top:24px}
.title{position:absolute;left:0;width:100%;text-align:center;color:#fff;font-size:22px;font-weight:600}
.photo{position:absolute;border-radius:6px}
.ribbon{position:absolute;background:var(--orange);color:#fff;text-align:right;padding:4px 10px 0 0;clip-path:polygon(8% 0,100% 0,100% 100%,0 100%)}
.ribbon small{display:block;font-size:13px;line-height:15px}
.ribbon b{display:block;font-size:19px;font-weight:600;line-height:24px}
.card{position:absolute;background:#fff}
.dish{position:absolute;font-size:24px;font-weight:600}
.price{position:absolute;color:var(--orange);font-weight:600}
.addr{position:absolute;font-size:13px;color:#444;display:flex;align-items:center;gap:6px}
.addr em{font-style:normal;color:#aaa}
.bold-line{position:absolute;font-size:15px;font-weight:600}
.rating{position:absolute;font-size:13px;color:#666}
.rating i{color:var(--orange);font-style:normal}
.circle{position:absolute;border-radius:50%}
.cat{position:absolute;width:60px;height:60px;border:1.5px solid #ddd;border-radius:50%;display:flex;align-items:center;justify-content:center}
.cat-name{position:absolute;width:90px;text-align:center;font-size:13px;color:#333}
.tab{position:absolute;font-size:16px;font-weight:500;color:var(--green)}
.pill{position:absolute;width:50px;height:24px;border:1px solid #ccc;border-radius:12px;font-size:13px;color:#888;text-align:center;line-height:22px}
.thumb{position:absolute;width:78px;height:84px;border-radius:2px}
.thumb-name{position:absolute;width:84px;text-align:center;font-size:13px;color:#444}
.section{position:absolute;font-size:16px;font-weight:500}
.ingredient{position:absolute;left:19px;font-size:13px;font-weight:500;color:#222}
.spec{position:absolute;font-size:13px}
</style>
</head>
<body>
<div class="stage">

  <div class="brand">Tavi Lo</div>

  <div class="label-big" style="left:1090px;top:64px">Restaurant Details</div>
  <div class="dash-h" style="left:1020px;top:90px;width:50px"></div>
  <div class="label-big" style="left:1130px;top:284px">Plate Details</div>

  <!-- Restaurants list screen -->
  <section class="screen" style="left:65px;top:237px;height:955px;background:var(--light)">
    <div class="header" style="height:131px">
      <div class="time">9:30</div>
      <svg class="status" width="70" height="14" viewBox="0 0 70 14"><g fill="#fff"><rect x="0" y="9" width="3" height="5"/><rect x="5" y="6" width="3" height="8"/><rect x="10" y="3" width="3" height="11"/><rect x="15" y="0" width="3" height="14"/><path d="M26 5a10 10 0 0 1 14 0l-2 2a7 7 0 0 0-10 0zM30 9a4 4 0 0 1 6 0l-3 4z"/><rect x="44" y="1" width="24" height="12" rx="3" fill="none" stroke="#fff" stroke-width="1.5"/><rect x="46" y="3" width="19" height="8" rx="1"/></g></svg>
      <div class="abs" style="left:18px;top:82px;color:#fff;font-size:14px;font-weight:600">Tavi Lo</div>
      <div class="title" style="top:74px">Restaurants</div>
      <svg class="abs" style="left:387px;top:80px" width="24" height="24" viewBox="0 0 24 24"><circle cx="10" cy="10" r="8" fill="none" stroke="#fff" stroke-width="2"/><path d="M16 16l6 6" stroke="#fff" stroke-width="2"/></svg>
    </div>

    <article class="card" style="left:8px;top:151px;width:420px;height:355px">
      <div class="circle" style="left:16px;top:16px;width:38px;height:38px;background:#f4e8e1;border:1px solid #e3d2c8"></div>
      <div class="abs" style="left:67px;top:16px;font-size:16px;font-weight:500">Restaurant Palatia</div>
      <div class="rating" style="left:67px;top:38px"><i>★</i> 4.9 (245)</div>
      <div class="ribbon" style="left:305px;top:9px;width:122px;height:50px"><small>Today!</small><b>10:15 am</b></div>
      <div class="photo" role="img" aria-label="Roasted chicken legs with tomatoes on a white plate" style="left:0;top:69px;width:420px;height:165px;border-radius:0;background:linear-gradient(120deg,#d8d8d6 0%,#ececea 40%,#7a4a2a 62%,#e9e9e7 85%)"></div>
      <div class="dish" style="left:15px;top:242px">Chicken Stroganoff</div>
      <div class="price" style="right:16px;top:250px;font-size:18px">$ 120</div>
      <div class="abs" style="right:16px;top:271px;font-size:12px;color:#555">2 People</div>
      <div class="addr" style="left:15px;top:281px"><svg width="14" height="14" viewBox="0 0 14 14"><path d="M7 1a4.5 4.5 0 0 1 4.5 4.5C11.5 9 7 13 7 13S2.5 9 2.5 5.5A4.5 4.5 0 0 1 7 1z" fill="none" stroke="#777"/><circle cx="7" cy="5.5" r="1.5" fill="none" stroke="#777"/></svg>Shop No. 27, Ground Floor, Q9 Mall, <em>2.8 km</em></div>
      <div class="bold-line" style="left:15px;top:318px">Get to know more dishes now!</div>
    </article>

    <article class="card" style="left:8px;top:520px;width:420px;height:380px">
      <div class="circle" style="left:16px;top:16px;width:38px;height:38px;background:#f6c514;border:2px solid #333"></div>
      <div class="abs" style="left:67px;top:16px;font-size:16px;font-weight:500">Good Fork Cafe or restaurant</div>
      <div class="rating" style="left:67px;top:38px"><i>★</i> 4.5 (625)</div>
      <div class="ribbon" style="left:305px;top:9px;width:122px;height:50px"><small>Today!</small><b>10:05 am</b></div>
      <div class="photo" role="img" aria-label="Spaghetti with tomato sauce, meatballs and basil in a blue plate" style="left:0;top:68px;width:420px;height:165px;border-radius:0;background:linear-gradient(110deg,#6b2a17 0%,#9b3a1c 35%,#d97a2a 60%,#4e86a0 100%)"></div>
      <div class="dish" style="left:15px;top:242px">Italian-pasta</div>
      <div class="price" style="right:16px;top:249px;font-size:18px">$ 120</div>
      <div class="addr" style="left:15px;top:281px"><svg width="14" height="14" viewBox="0 0 14 14"><path d="M7 1a4.5 4.5 0 0 1 4.5 4.5C11.5 9 7 13 7 13S2.5 9 2.5 5.5A4.5 4.5 0 0 1 7 1z" fill="none" stroke="#777"/><circle cx="7" cy="5.5" r="1.5" fill="none" stroke="#777"/></svg>Shop No. 27, Ground Floor, Q9 Mall, <em>2.8 km</em></div>
      <div class="bold-line" style="left:15px;top:317px;width:390px;line-height:19px">italian pasta with tomato sauce and meatballsin blue plate</div>
    </article>

    <nav class="abs" style="left:0;top:893px;width:440px;height:62px;background:#fff;border-top:1px solid #eee">
      <div class="abs" style="left:14px;top:20px;font-size:12px;font-weight:700;color:var(--plum)">Tavi Lo</div>
      <svg class="abs" style="left:110px;top:20px" width="26" height="22" viewBox="0 0 26 22"><path d="M13 21S1 13 1 6.5A5.5 5.5 0 0 1 13 4a5.5 5.5 0 0 1 12 2.5C25 13 13 21 13 21z" fill="none" stroke="#888" stroke-width="1.5"/></svg>
      <svg class="abs" style="left:204px;top:18px" width="24" height="26" viewBox="0 0 24 26"><path d="M4 19V11a8 8 0 0 1 16 0v8l2 2H2zM9 23a3 3 0 0 0 6 0" fill="none" stroke="#888" stroke-width="1.5"/></svg>
      <svg class="abs" style="left:299px;top:18px" width="22" height="26" viewBox="0 0 22 26"><circle cx="11" cy="8" r="6" fill="none" stroke="#888" stroke-width="1.5"/><path d="M1 25a10 9 0 0 1 20 0z" fill="none" stroke="#888" stroke-width="1.5"/></svg>
      <svg class="abs" style="left:390px;top:20px" width="24" height="22" viewBox="0 0 24 22"><g stroke="#888" stroke-width="1.5" fill="none"><path d="M1 4h22M1 11h22M1 18h22"/><circle cx="7" cy="4" r="2.5" fill="#fff"/><circle cx="16" cy="11" r="2.5" fill="#fff"/><circle cx="9" cy="18" r="2.5" fill="#fff"/></g></svg>
    </nav>
  </section>

  <div class="dash-v" style="left:94px;top:1222px;height:30px"></div>
  <div class="note" style="left:47px;top:1254px">Restaurants</div>
  <div class="dash-v" style="left:188px;top:1222px;height:62px"></div>
  <div class="note" style="left:141px;top:1288px">Favorites Rest.</div>
  <div class="dash-v" style="left:282px;top:1222px;height:28px"></div>
  <div class="note" style="left:234px;top:1252px">Notifications</div>
  <div class="dash-v" style="left:376px;top:1222px;height:10px"></div>
  <div class="note" style="left:352px;top:1234px">Profile</div>
  <div class="dash-v" style="left:467px;top:1222px;height:30px"></div>
  <div class="note" style="left:419px;top:1253px">App Settings</div>

  <!-- Restaurant details screen -->
  <section class="screen" style="left:563px;top:58px;height:1342px">
    <div class="header" style="height:327px"></div>
    <div class="time">9:30</div>
    <svg class="status" width="70" height="14" viewBox="0 0 70 14"><g fill="#fff"><rect x="0" y="9" width="3" height="5"/><rect x="5" y="6" width="3" height="8"/><rect x="10" y="3" width="3" height="11"/><rect x="15" y="0" width="3" height="14"/><path d="M26 5a10 10 0 0 1 14 0l-2 2a7 7 0 0 0-10 0zM30 9a4 4 0 0 1 6 0l-3 4z"/><rect x="44" y="1" width="24" height="12" rx="3" fill="none" stroke="#fff" stroke-width="1.5"/><rect x="46" y="3" width="19" height="8" rx="1"/></g></svg>
    <svg class="abs" style="left:22px;top:70px" width="28" height="24" viewBox="0 0 28 24"><path d="M27 12H3M12 2L2 12l10 10" fill="none" stroke="#fff" stroke-width="2"/></svg>
    <div class="title" style="top:70px">Details</div>
    <svg class="abs" style="left:390px;top:68px" width="34" height="30" viewBox="0 0 26 22"><path d="M13 21S1 13 1 6.5A5.5 5.5 0 0 1 13 4a5.5 5.5 0 0 1 12 2.5C25 13 13 21 13 21z" fill="none" stroke="#fff" stroke-width="1.6"/></svg>
    <div class="photo" role="img" aria-label="Salad bowl with avocado, quinoa, tomatoes and grilled chicken on a wooden table" style="left:18px;top:139px;width:382px;height:239px;background:radial-gradient(circle at 45% 50%,#e9e4d2 0 30%,#7aa83e 40%,#c94a2c 52%,#4a2a1c 70%)"></div>
    <div class="photo" role="img" aria-label="Next dish photo" style="left:411px;top:139px;width:40px;height:239px;background:linear-gradient(90deg,#e8e6e2,#cfcbc4)"></div>

    <div class="abs" style="left:21px;top:395px;font-size:21px;font-weight:500">Restaurant Palatia</div>
    <div class="rating" style="right:22px;top:400px"><i>★</i> 4.9 (245)</div>
    <div class="addr" style="left:21px;top:428px"><svg width="14" height="14" viewBox="0 0 14 14"><path d="M7 1a4.5 4.5 0 0 1 4.5 4.5C11.5 9 7 13 7 13S2.5 9 2.5 5.5A4.5 4.5 0 0 1 7 1z" fill="none" stroke="#777"/><circle cx="7" cy="5.5" r="1.5" fill="none" stroke="#777"/></svg>Shop No. 27, Ground Floor, Q9 Mall</div>
    <div class="abs" style="left:21px;top:468px;font-size:16px;font-weight:500">Open Now<sup style="color:var(--orange);font-size:9px">•</sup> 12 noon - 11:29 pm(Today)</div>
    <div class="abs" style="left:21px;top:493px;font-size:13px;color:#444">Opening hours Mon-Sun&nbsp; 12 Noon - 10:30 am</div>

    <div class="cat" style="left:22px;top:540px"><svg width="30" height="30" viewBox="0 0 30 30"><path d="M4 16a11 11 0 0 0 22 0zM8 12l7-8 7 8" fill="none" stroke="var(--orange)" stroke-width="1.5"/></svg></div>
    <div class="cat" style="left:99px;top:540px"><svg width="30" height="30" viewBox="0 0 30 30"><path d="M4 14a11 10 0 0 0 22 0zM6 10h18M10 6h10" fill="none" stroke="var(--orange)" stroke-width="1.5"/></svg></div>
    <div class="cat" style="left:175px;top:540px"><svg width="30" height="30" viewBox="0 0 30 30"><path d="M4 18a11 9 0 0 0 22 0zM10 14c0-5 10-5 10 0" fill="none" stroke="var(--orange)" stroke-width="1.5"/></svg></div>
    <div class="cat" style="left:251px;top:540px"><svg width="30" height="30" viewBox="0 0 30 30"><path d="M3 15c6-8 16-8 20 0-4 8-14 8-20 0zM23 15l5-5v10z" fill="none" stroke="var(--orange)" stroke-width="1.5"/></svg></div>
    <div class="cat" style="left:328px;top:540px"><svg width="30" height="30" viewBox="0 0 30 30"><path d="M7 8h14v16H7zM21 12h4v6h-4" fill="none" stroke="var(--orange)" stroke-width="1.5"/></svg></div>
    <div class="cat" style="left:404px;top:540px"><svg width="30" height="30" viewBox="0 0 30 30"><path d="M4 20h22M6 20a9 7 0 0 1 18 0" fill="none" stroke="var(--orange)" stroke-width="1.5"/></svg></div>
    <div class="cat-name" style="left:7px;top:603px">Mexican</div>
    <div class="cat-name" style="left:84px;top:603px">Asian</div>
    <div class="cat-name" style="left:160px;top:603px">Breakfast</div>
    <div class="cat-name" style="left:236px;top:603px">Sea Food</div>
    <div class="cat-name" style="left:313px;top:603px">Cafe</div>
    <div class="cat-name" style="left:389px;top:603px">Back</div>

    <div class="tab" style="left:21px;top:651px">Map</div>
    <div class="tab" style="left:74px;top:651px">Today’s Menu</div>
    <div class="abs" style="left:71px;top:677px;width:120px;border-top:2px solid var(--green)"></div>
    <div class="tab" style="left:205px;top:651px">246 Reviews</div>
    <div class="tab" style="left:334px;top:651px">189 Photos</div>

    <article class="card" style="left:15px;top:692px;width:411px;height:120px;border-radius:8px;box-shadow:0 2px 10px rgba(0,0,0,.12)">
      <div class="dish" style="left:20px;top:14px">Chicken Stroganoff</div>
      <div class="bold-line" style="left:20px;top:49px;font-size:14px">Get to know more dishes now!</div>
      <div class="abs" style="left:22px;top:73px;font-size:13px;color:#555">2 People <span style="color:var(--orange);font-weight:600;font-size:17px;margin-left:6px">$ 120</span></div>
      <div class="ribbon" style="left:296px;top:10px;width:121px;height:48px"><small>Today!</small><b>10:15 am</b></div>
    </article>

    <div class="abs" style="left:20px;top:821px;width:402px;height:50px;background:var(--plum-dark);color:#fff;font-size:16px;font-weight:500;text-align:center;line-height:50px">More in Menu
      <svg class="abs" style="right:16px;top:17px" width="22" height="16" viewBox="0 0 22 16"><path d="M1 8h19M13 1l7 7-7 7" fill="none" stroke="#fff" stroke-width="1.6"/></svg>
    </div>

    <div class="section" style="left:21px;top:894px">Rate this place</div>
    <div class="pill" style="left:21px;top:927px"><span style="color:#bbb">★</span> 1</div>
    <div class="pill" style="left:76px;top:927px"><span style="color:#bbb">★</span> 2</div>
    <div class="pill" style="left:130px;top:927px"><span style="color:#bbb">★</span> 3</div>
    <div class="pill" style="left:183px;top:927px"><span style="color:#bbb">★</span> 4</div>
    <div class="pill" style="left:236px;top:927px"><span style="color:#bbb">★</span> 5</div>

    <div class="section" style="left:21px;top:974px">Menu</div>
    <div class="thumb" role="img" aria-label="Burger menu card" style="left:21px;top:999px;background:linear-gradient(135deg,#f4b81c,#c9311e)"></div>
    <div class="thumb" role="img" aria-label="Hand-drawn restaurant menu" style="left:104px;top:999px;background:linear-gradient(135deg,#9a9a9a,#2c2c2c)"></div>
    <div class="thumb" role="img" aria-label="Sketched menu page" style="left:187px;top:999px;background:linear-gradient(135deg,#e8e8e8,#7a7a7a)"></div>
    <div class="thumb" role="img" aria-label="Fast food menu card" style="left:270px;top:999px;background:linear-gradient(135deg,#f2e6d2,#d2452a)"></div>
    <div class="thumb" role="img" aria-label="More menu cards" style="left:353px;top:999px;background:linear-gradient(135deg,#8a5a1a,#3a2410)">
      <div style="color:#fff;font-size:26px;font-weight:500;text-align:center;line-height:84px">+6</div>
    </div>

    <div class="section" style="left:21px;top:1107px">Photos</div>
    <div class="thumb" role="img" aria-label="Chicken dish photo" style="left:21px;top:1132px;background:linear-gradient(135deg,#e6e4e0,#8a4a26)"></div>
    <div class="thumb" role="img" aria-label="Fresh salad photo" style="left:104px;top:1132px;background:linear-gradient(135deg,#3f6e22,#c8402a)"></div>
    <div class="thumb" role="img" aria-label="Table with bowl photo" style="left:187px;top:1132px;background:linear-gradient(135deg,#d8d6d2,#b88a5a)"></div>
    <div class="thumb" style="left:270px;top:1132px;background:#d8d8d8;display:flex;align-items:center;justify-content:center">
      <svg width="32" height="26" viewBox="0 0 32 26"><path d="M2 7h7l3-5h8l3 5h7v17H2z" fill="#888"/><circle cx="16" cy="15" r="5.5" fill="#d8d8d8"/><circle cx="16" cy="15" r="3.5" fill="#888"/></svg>
    </div>
    <div class="thumb-name" style="left:18px;top:1220px">Food</div>
    <div class="thumb-name" style="left:101px;top:1220px">Ambience</div>
    <div class="thumb-name" style="left:184px;top:1220px">All(652)</div>
    <div class="thumb-name" style="left:267px;top:1220px">Add Photo</div>

    <div class="section" style="left:21px;top:1267px">Details</div>
    <div class="abs" style="left:21px;top:1305px;font-size:13px;color:#9a8a2a">CALL</div>
    <div class="abs" style="left:21px;top:1322px;font-size:13px;color:var(--green)">030000000</div>
    <div class="circle" style="left:390px;top:1306px;width:28px;height:28px;background:#4a9a3a">
      <svg class="abs" style="left:7px;top:7px" width="14" height="14" viewBox="0 0 14 14"><path d="M3 1l2 3-1.5 1.5a8 8 0 0 0 5 5L10 9l3 2-1 2c-6 0-11-5-11-11z" fill="#fff"/></svg>
    </div>
  </section>

  <div class="dash-v" style="left:693px;top:1390px;height:32px"></div>
  <div class="dash-h" style="left:530px;top:1422px;width:163px"></div>
  <div class="note" style="left:226px;top:1406px;line-height:20px">Scroll to see more details of restaurant<br>(like) Address, which foods people liked most,<br>Top dishes order by people,Facilities (wifi, home delivery, smoking area etc.)<br>and Rateing &amp; Reviews.</div>

  <!-- Plate details screen -->
  <section class="screen" style="left:1030px;top:365px;height:1032px">
    <div class="header" style="height:133px"></div>
    <div class="time">9:30</div>
    <svg class="status" width="70" height="14" viewBox="0 0 70 14"><g fill="#fff"><rect x="0" y="9" width="3" height="5"/><rect x="5" y="6" width="3" height="8"/><rect x="10" y="3" width="3" height="11"/><rect x="15" y="0" width="3" height="14"/><path d="M26 5a10 10 0 0 1 14 0l-2 2a7 7 0 0 0-10 0zM30 9a4 4 0 0 1 6 0l-3 4z"/><rect x="44" y="1" width="24" height="12" rx="3" fill="none" stroke="#fff" stroke-width="1.5"/><rect x="46" y="3" width="19" height="8" rx="1"/></g></svg>
    <svg class="abs" style="left:22px;top:86px" width="28" height="24" viewBox="0 0 28 24"><path d="M27 12H3M12 2L2 12l10 10" fill="none" stroke="#fff" stroke-width="2"/></svg>
    <div class="title" style="top:84px">Details</div>
    <svg class="abs" style="left:390px;top:84px" width="34" height="30" viewBox="0 0 26 22"><path d="M13 21S1 13 1 6.5A5.5 5.5 0 0 1 13 4a5.5 5.5 0 0 1 12 2.5C25 13 13 21 13 21z" fill="none" stroke="#fff" stroke-width="1.6"/></svg>
    <div class="photo" role="img" aria-label="Roasted chicken legs with tomatoes on a white plate" style="left:15px;top:152px;width:368px;height:251px;border-radius:0;background:radial-gradient(circle at 60% 50%,#7a4a2a 0 22%,#f4f4f2 38%,#d6d6d4 60%)"></div>
    <div class="photo" role="img" aria-label="Next dish photo" style="left:393px;top:152px;width:47px;height:251px;border-radius:0;background:linear-gradient(180deg,#e8e2da,#c9a27a,#d23a2a)"></div>

    <div class="dish" style="left:17px;top:424px;font-size:25px">Chicken Stroganoff</div>
    <div class="price" style="right:26px;top:422px;font-size:26px">$ 120</div>
    <div class="rating" style="left:19px;top:459px"><i>★</i> 4.9 (245)</div>
    <div class="abs" style="right:26px;top:455px;font-size:13px;color:#555">2 People</div>
    <div class="abs" style="left:20px;top:498px;width:405px;font-size:13px;line-height:16px;color:#333">Chicken Stroganoff - this stuff is so delicious and is a recipe perfect for dinner any night. Tastes better than restaurant Stroganoff!!</div>

    <div class="spec" style="left:21px;top:551px;font-weight:500">Course</div>
    <div class="spec" style="left:107px;top:551px;color:#555">Main Course</div>
    <div class="spec" style="left:21px;top:572px;font-weight:500">Cuisine</div>
    <div class="spec" style="left:107px;top:572px;color:#555">American</div>
    <div class="spec" style="left:21px;top:593px;font-weight:500">Calories</div>
    <div class="spec" style="left:107px;top:593px;color:#555">3403 kcal</div>

    <div class="abs" style="left:17px;top:638px;font-size:24px;font-weight:600">Ingredients</div>
    <div class="ingredient" style="top:690px">Kosher salt</div>
    <div class="ingredient" style="top:714px">3 tablespoons unsalted butter</div>
    <div class="ingredient" style="top:741px">1 small onion, chopped</div>
    <div class="ingredient" style="top:772px">4 ounces white or cremini mushrooms, sliced (about 2 cups)</div>
    <div class="ingredient" style="top:802px">1 1/4 pounds skinless, boneless chicken thighs, cut into chunks</div>
    <div class="ingredient" style="top:834px">2 tablespoons all-purpose flour</div>
    <div class="ingredient" style="top:872px">1 teaspoon paprika, plus more for topping</div>
    <div class="ingredient" style="top:913px">Freshly ground pepper</div>
    <div class="ingredient" style="top:955px;color:#bbb">1 cup fat-free low-sodium chicken or mushroom broth</div>

    <div class="abs" style="left:260px;top:905px;width:160px;height:40px;border-radius:20px;background:var(--orange);color:#fff;font-size:15px;font-weight:500;text-align:center;line-height:40px;box-shadow:0 3px 8px rgba(0,0,0,.2)">Reserve a Table</div>

    <div class="abs" style="left:0;top:987px;width:440px;height:45px;background:#eee;text-align:center;font-size:13px;font-weight:500;line-height:45px">View All
      <svg width="14" height="8" viewBox="0 0 14 8" style="margin-left:6px"><path d="M1 1l6 6 6-6" fill="none" stroke="#333" stroke-width="1.4"/></svg>
    </div>
  </section>

</div>
</body>
</html>
```